Just to be clear - I have the domain and the wordpress site (which is messy). I need someone to help me complete a simple blog design and then go into the existing wordpress site, and get rid of all the existing rubbish and set up the templates please. If we progress with design can we please be clear about additional costs upfront which, of course, I appreciate is the case.

Need a lifestyle blog. It is called brightyearsahead.com. Aimed at the older woman but needs to look fresh and young, not old fashioned. Navigation will be Home, Fashion, Feelings, Fitness, Contact. I have a logo but not sure it will work at the moment so happy with stylised words.Will have social media links.

Need homepage (not overly long) to have a main slider for pics/videos. Then the three category boxes underneath linking through to 2nd level pages containing blogs for that category and then the actual blog page. Happy to be led by expertise if this is not gonna work.

Am really looking for something clean and fresh like a Marvette type approach to be honest.

If you need any further direction please just ask - once design chosen I am looking to move quickly.

Thank you so much for looking at this brief

Target Market(s)

Women, 40 - 60 age group but with a younger outlook

Colors

Requirements
Must have
• Reflect youth, fun, bright
• Lift easily into a wordpress format
Should not have
• Old, staid, frumpy,dark

```html
<!DOCTYPE html>
<html lang="en">
<head>
<meta charset="utf-8">
<title>The Holistic Benefits of Ustrasana (Camel Pose) – brightyearsahead.com</title>
<link rel="stylesheet" href="https://fonts.googleapis.com/css2?family=Josefin+Sans:wght@400;600;700&family=Open+Sans:ital,wght@0,400;0,600;0,700;1,400&family=Dancing+Script:wght@600&display=swap">
<style>
:root{
  --ink:#1b1b1b;
  --text:#6a6a6a;
  --muted:#9a9a9a;
  --pink:#ee4a95;
  --frame:#b9d4df;
  --label:#86b6c9;
  --panel:#f3f4f3;
  --rule:#e3e3e3;
  --white:#ffffff;
}
*{box-sizing:border-box;margin:0;padding:0}
html,body{width:1200px;height:2586px;overflow:hidden;background:var(--white)}
body{position:relative;font-family:"Open Sans",sans-serif;color:var(--text)}
.head-font{font-family:"Josefin Sans",sans-serif}

/* header */
.site-header{position:absolute;top:0;left:0;width:1200px;height:80px}
.nav-link{position:absolute;top:30px;font-family:"Josefin Sans",sans-serif;font-size:13px;letter-spacing:.6px;color:var(--ink);text-transform:uppercase}
.site-logo{position:absolute;top:20px;left:0;width:1200px;text-align:center;font-family:"Josefin Sans",sans-serif;font-weight:600;font-size:25px;letter-spacing:.5px;color:var(--ink);text-transform:uppercase}

/* article */
.post{position:absolute;left:93px;top:0;width:697px}
.post-title-box{position:absolute;left:36px;top:93px;width:625px;height:188px;border:2px solid var(--frame);z-index:2;text-align:center}
.post-cats{margin-top:20px;font-family:"Josefin Sans",sans-serif;font-weight:600;font-size:12px;letter-spacing:1px;color:var(--label)}
.post-cats span{margin:0 4px}
.post-title{margin-top:8px;font-family:"Josefin Sans",sans-serif;font-weight:600;font-size:31px;line-height:32px;color:var(--ink);letter-spacing:.5px}
.post-meta{margin-top:24px;font-size:10px;letter-spacing:.4px;text-transform:uppercase}
.post-meta .date{color:var(--muted);margin-right:14px}
.post-meta .author{color:var(--ink);font-weight:600}
.hero-photo{position:absolute;left:0;top:247px;width:697px;height:468px;background:linear-gradient(180deg,#375d73 0%,#5f8aa0 35%,#a9c3cc 52%,#d9dcd6 60%,#b2a595 75%,#8f8273 100%)}
.post-body{position:absolute;left:0;top:756px;width:697px;font-size:13.4px;line-height:19.6px}
.post-body p{margin-bottom:11px}
.post-body h2{font-family:"Josefin Sans",sans-serif;font-weight:600;font-size:17px;color:var(--ink);letter-spacing:.6px;margin:18px 0 9px}
.benefits{list-style:none;margin-bottom:17px}
.benefits li{position:relative;padding-left:17px}
.benefits li::before{content:"";position:absolute;left:3px;top:8px;width:5px;height:5px;border-radius:50%;background:var(--text)}
.pull-quote{margin:27px 0 40px 106px;width:485px;height:234px;border:2px solid var(--frame);padding:40px 36px 0;text-align:center}
.pull-quote q{display:block;quotes:none;font-weight:700;font-size:17.5px;line-height:24px;color:var(--ink);text-transform:uppercase}
.pull-quote cite{display:block;margin-top:26px;font-style:normal;font-size:12.5px;color:var(--muted)}
.post-tags{position:absolute;left:0;top:1710px;display:flex;gap:10px}
.tag{border:1px solid var(--rule);padding:6px 12px;font-size:10.5px;font-weight:700;letter-spacing:.6px;color:var(--ink)}
.post-divider{position:absolute;left:0;top:1750px;width:697px;border-top:1px solid var(--rule)}
.share{position:absolute;left:0;top:1773px;width:697px;display:flex;justify-content:center;align-items:center;gap:20px;font-size:10.5px;color:var(--ink)}
.share .share-label{letter-spacing:3px;font-size:9.5px;text-transform:uppercase;margin-right:6px}
.share .net{font-weight:700}
.post-nav{position:absolute;top:1856px;width:334px;height:132px;background:var(--panel);text-align:center;padding-top:28px}
.post-nav .nav-label{font-family:"Josefin Sans",sans-serif;font-weight:600;font-size:11px;letter-spacing:.6px;color:var(--label);text-transform:uppercase}
.post-nav .nav-title{margin-top:8px;font-family:"Josefin Sans",sans-serif;font-weight:600;font-size:18px;color:var(--ink);text-transform:uppercase}
.comments{position:absolute;left:0;top:2042px;width:697px}
.comments h3{font-family:"Josefin Sans",sans-serif;font-weight:600;font-size:17px;color:var(--ink);letter-spacing:.5px;text-transform:uppercase}
.comments .leave{margin-top:22px}
.comments .note{margin-top:5px;font-size:10px;color:var(--muted)}
.field{position:absolute;background:var(--panel);font-size:11px;color:var(--muted);padding:12px 12px}
.submit{position:absolute;left:491px;top:349px;width:206px;height:41px;background:var(--pink);color:var(--white);font-family:"Josefin Sans",sans-serif;font-weight:700;font-size:12px;letter-spacing:.5px;display:flex;align-items:center;justify-content:center;text-transform:uppercase}

/* sidebar */
.sidebar{position:absolute;left:860px;top:0;width:239px}
.about-box{position:absolute;left:0;top:172px;width:239px;height:373px;border:2px solid var(--frame);text-align:center}
.avatar{position:absolute;left:35px;top:80px;width:170px;height:170px;border-radius:50%;background:radial-gradient(circle at 50% 40%,#c97a5a 0%,#a4502f 45%,#e9e4e1 80%);border:4px solid var(--white);z-index:2}
.widget-title{position:absolute;left:0;width:239px;text-align:center;font-family:"Josefin Sans",sans-serif;font-weight:700;font-size:12.5px;letter-spacing:.6px;color:var(--ink);text-transform:uppercase}
.widget-title::after{content:"";display:block;width:56px;margin:8px auto 0;border-top:2px solid #f6b3d1}
.about-text{position:absolute;left:12px;top:303px;width:215px;text-align:center;font-style:italic;font-size:12.4px;line-height:21.2px;color:#7a6e68}
.follow-script{position:absolute;left:0;top:472px;width:239px;text-align:center;font-family:"Dancing Script",cursive;font-size:22px;color:var(--label)}
.social-row{position:absolute;left:0;top:506px;width:239px;display:flex;justify-content:center;gap:10px;font-size:10px;font-weight:700;color:var(--ink)}
.input{position:absolute;left:0;width:239px;height:42px;background:var(--panel);font-size:11px;color:var(--muted);padding:13px 12px}
.signup{position:absolute;left:0;top:684px;width:239px;height:38px;background:var(--pink);color:var(--white);font-family:"Josefin Sans",sans-serif;font-weight:700;font-size:12px;letter-spacing:.5px;display:flex;align-items:center;justify-content:center}
.insta-grid{position:absolute;left:0;top:800px;width:239px;display:grid;grid-template-columns:repeat(3,74px);gap:8px 8.5px}
.insta-grid div{height:74px}
.cat-list{position:absolute;left:0;top:1120px;width:239px;list-style:none}
.cat-list li{height:42.5px;border-bottom:1px solid var(--rule);font-size:12.5px;color:var(--ink);padding-top:11px}
.cat-list li.current{color:#3d87a8}
.recent{position:absolute;left:0;width:239px;display:flex;gap:14px}
.recent .thumb{width:62px;height:62px;flex:none}
.recent .date{font-size:10px;color:var(--muted);line-height:13px}
.recent .title{font-family:"Josefin Sans",sans-serif;font-weight:600;font-size:11.5px;line-height:14px;color:var(--ink);text-transform:uppercase}
.search{position:absolute;left:0;top:1894px;width:239px;height:42px;background:var(--panel)}
.search span{position:absolute;left:12px;top:13px;font-size:11px;color:var(--muted)}
.search .btn{position:absolute;right:0;top:0;width:42px;height:42px;background:var(--pink);display:flex;align-items:center;justify-content:center}
.banner{position:absolute;left:0;top:2011px;width:239px;height:324px;background:linear-gradient(135deg,#d9d7d0 0%,#b9b6ad 40%,#e6e2dc 70%,#e8d3c8 100%)}
.banner-word{position:absolute;left:0;top:130px;width:239px;text-align:center;font-family:"Josefin Sans",sans-serif;font-size:46px;letter-spacing:2px;color:var(--white)}
.banner-sub{position:absolute;left:22px;top:272px;font-family:"Dancing Script",cursive;font-size:17px;color:#333}

/* footer */
.site-footer{position:absolute;left:93px;top:2496px;width:1006px;border-top:1px solid #8d8d8d}
.footer-link{position:absolute;top:36px;font-family:"Josefin Sans",sans-serif;font-size:13px;letter-spacing:.6px;color:var(--ink)}
.footer-logo{position:absolute;left:0;top:24px;width:1006px;text-align:center;font-family:"Josefin Sans",sans-serif;font-weight:600;font-size:25px;letter-spacing:.5px;color:var(--ink)}
.footer-social{position:absolute;right:0;top:36px;display:flex;gap:12px;font-size:11px;font-weight:700;color:var(--ink)}
</style>
</head>
<body>

<header class="site-header">
  <span class="nav-link" style="left:153px">Home</span>
  <span class="nav-link" style="left:226px">Fashion</span>
  <span class="nav-link" style="left:324px">Feelings</span>
  <div class="site-logo">brightyearsahead.com</div>
  <span class="nav-link" style="left:794px">Videos</span>
  <span class="nav-link" style="left:870px">Fitness</span>
  <span class="nav-link" style="left:950px">Contact</span>
</header>

<main class="post">
  <div class="post-title-box">
    <div class="post-cats"><span>HEALTH</span><span>YOGA</span></div>
    <h1 class="post-title">THE HOLISTIC BENEFITS OF<br>USTRASANA (CAMEL POSE)</h1>
    <div class="post-meta"><span class="date">May 5, 2016</span><span class="author">By Lena Hartwell</span></div>
  </div>
  <div class="hero-photo" role="img" aria-label="Woman in a yoga headstand pose on a patterned mat on the beach by the sea"></div>

  <div class="post-body">
    <p>There are poses in yoga that benefit almost all the body systems. Camels Pose is one of them. Do it the right way and it will bring you lots of benefits on physical, mental and emotional levels.</p>
    <h2>HOW TO DO</h2>
    <p>Sit on knees, make sure your thighs are perpendicular to the floor and your knees are a hip-width apart. Check that your soles face upward and your toes are touching the floor. &nbsp;Put your hands on your sacrum or on your hips. Inhale and start arching your back, move your hands from hips (sacrum) to your heels one by one. And if your neck feels alright, throw back your head.</p>
    <h2>BENEFITS</h2>
    <ul class="benefits">
      <li>Increases spine flexibility and improves posture</li>
      <li>Stimulates the thyroid gland</li>
      <li>Normalises the digestion</li>
      <li>Relieves tension in shoulders, back, and neck</li>
      <li>Improves respiration by opening up chest</li>
      <li>Stretches hips and abdominal muscles</li>
    </ul>
    <p>In addition to all the above, Camel Pose has a great effect on your mental and emotional health.</p>
    <p>It is a great stress reliever. Have you noticed how you start slouching when you are burdened with problems? By relaxing your spine in Camel Pose you are letting go of stress and anxiety. The pose also opens up heart chakra and brings suppressed emotions to the forefront. Some people even start crying in this pose. So, Ustrasana is a good way to deal with emotions.</p>
    <blockquote class="pull-quote">
      <q>Mindfulness helps you go home to the present. And every time you go there and recognize a condition of happiness that you have, happiness comes</q>
      <cite>Anna Lindqvist</cite>
    </blockquote>
    <p>As you see, yoga has a very beautiful pose to bring your body, mind, and soul in harmony. Stay in this pose for the maximum of 20 seconds when starting, you can then increase the time up to 30-60 seconds. And don't forget to breathe deeply.</p>
    <p style="margin-top:17px">Source: www.stretchandbreathe.com</p>
  </div>

  <div class="post-tags"><span class="tag">LIFESTYLE</span><span class="tag">YOGA</span></div>
  <div class="post-divider"></div>
  <div class="share"><span class="share-label">Share</span><span class="net">Kite</span><span class="net">Pinna</span><span class="net">Orbit</span></div>

  <a class="post-nav" style="left:0"><div class="nav-label">Previous Post</div><div class="nav-title">Girls Just Wanna Have Fun!</div></a>
  <a class="post-nav" style="left:363px"><div class="nav-label">Next Post</div><div class="nav-title">Think Green! Eat Green!</div></a>

  <section class="comments">
    <h3>0 Comments</h3>
    <h3 class="leave">Leave a Comment</h3>
    <p class="note">Your email address will not be published.</p>
    <div class="field" style="left:0;top:113px;width:697px;height:154px">Your Comment *</div>
    <div class="field" style="left:0;top:286px;width:334px;height:44px">Name *</div>
    <div class="field" style="left:363px;top:286px;width:334px;height:44px">Email *</div>
    <div class="submit">Post Your Comment</div>
  </section>
</main>

<aside class="sidebar">
  <div class="about-box"></div>
  <div class="avatar" role="img" aria-label="Portrait photo of the blog author"></div>
  <div class="widget-title" style="top:268px">About Me</div>
  <p class="about-text">Hi! Dummy text of the printing and typesetting industry. Lorem Ipsum has been the industry's standard dummy text ever since the 1500s Hi! Dummy text of the printing and typesetting industry. Lorem Ipsum has been the industry's standard dummy text ever since the 1500s</p>
  <div class="follow-script">follow me on</div>
  <div class="social-row"><span>Kite</span><span>Orbit</span><span>Loom</span><span>Prism</span><span>Halo</span></div>

  <div class="widget-title" style="top:577px">Newsletter</div>
  <div class="input" style="top:625px">Your email address</div>
  <div class="signup">SIGN UP</div>

  <div class="widget-title" style="top:750px">Follow@solene.theme</div>
  <div class="insta-grid">
    <div role="img" aria-label="Photo of shells and stones" style="background:linear-gradient(135deg,#6d6a55,#c4b79a)"></div>
    <div role="img" aria-label="Photo of pink flowers" style="background:linear-gradient(135deg,#f2d3cf,#e9b9b3)"></div>
    <div role="img" aria-label="Photo of a bright interior" style="background:linear-gradient(135deg,#f4f1ee,#b7aba3)"></div>
    <div role="img" aria-label="Photo of dark hair" style="background:linear-gradient(135deg,#5a4a44,#a08d85)"></div>
    <div role="img" aria-label="Photo of a wooden table" style="background:linear-gradient(135deg,#b59e8c,#e7dcd3)"></div>
    <div role="img" aria-label="Photo of pale blue paper" style="background:linear-gradient(135deg,#cfe0e4,#9fc0c7)"></div>
    <div role="img" aria-label="Photo of a beach" style="background:linear-gradient(135deg,#d9dee0,#9aa7ab)"></div>
    <div role="img" aria-label="Photo of palm leaves" style="background:linear-gradient(135deg,#3d3d3d,#c9c9c9)"></div>
    <div role="img" aria-label="Photo of a calm shoreline" style="background:linear-gradient(135deg,#f1efeb,#cfc9c0)"></div>
  </div>

  <div class="widget-title" style="top:1076px">Categories</div>
  <ul class="cat-list">
    <li>Beauty</li><li>Health</li><li class="current">Lifestyle</li><li>Music</li><li>Sport</li><li>Yoga</li>
  </ul>

  <div class="widget-title" style="top:1396px">Recent Posts</div>
  <div class="recent" style="top:1440px"><div class="thumb" role="img" aria-label="Photo of a person on a misty beach" style="background:linear-gradient(135deg,#eceae6,#c9c4bb)"></div><div><div class="date">June 1, 2016</div><div class="title">Why Learn to Meditate</div></div></div>
  <div class="recent" style="top:1529px"><div class="thumb" role="img" aria-label="Portrait photo of a singer" style="background:linear-gradient(135deg,#3c3c3c,#8d8d8d)"></div><div><div class="date">May 16, 2016</div><div class="title">Nova Rey - Critics Call<br>Her a New Ilsa Moon!</div></div></div>
  <div class="recent" style="top:1618px"><div class="thumb" role="img" aria-label="Photo of a green meal" style="background:linear-gradient(135deg,#5c6a60,#c9cfc6)"></div><div><div class="date">May 16, 2016</div><div class="title">Think Green! Eat Green!</div></div></div>
  <div class="recent" style="top:1704px"><div class="thumb" role="img" aria-label="Photo of a yoga pose on the beach" style="background:linear-gradient(180deg,#5f8aa0,#b2a595)"></div><div><div class="date">May 5, 2016</div><div class="title">The Holistic Benefits of<br>Ustrasana (Camel Pose)</div></div></div>
  <div class="recent" style="top:1793px"><div class="thumb" role="img" aria-label="Photo of friends having fun" style="background:linear-gradient(135deg,#6f6a66,#d3cdc6)"></div><div><div class="date">April 20, 2016</div><div class="title">Girls Just Wanna Have<br>Fun!</div></div></div>

  <div class="search"><span>Search...</span><div class="btn">
    <svg width="16" height="16" viewBox="0 0 16 16" aria-hidden="true"><circle cx="6.5" cy="6.5" r="4.8" fill="none" stroke="#fff" stroke-width="2"/><line x1="10" y1="10" x2="14.5" y2="14.5" stroke="#fff" stroke-width="2.2" stroke-linecap="round"/></svg>
  </div></div>

  <div class="widget-title" style="top:1962px">Banner</div>
  <div class="banner" role="img" aria-label="Advertising banner with soft pale palm leaves">
    <div class="banner-word">BANNER</div>
    <div class="banner-sub">place it here</div>
  </div>
</aside>

<footer class="site-footer">
  <span class="footer-link" style="left:0">ABOUT ME</span>
  <span class="footer-link" style="left:99px">CONTACT</span>
  <span class="footer-link" style="left:200px">DISCLAIMER</span>
  <div class="footer-logo">BRIGHTYEARSAHEAD.COM</div>
  <div class="footer-social"><span>Orbit</span><span>Kite</span><span>Prism</span><span>Reel</span><span>Quill</span></div>
</footer>

</body>
</html>
```